Stationary package for Real Estate Brokerage Ambervale Homes inc
Ambervale Homes - Brokerage Independently Owned and Operated
Stationary package for Real Estate Brokerage Ambervale Homes inc - Real Estate
Creative Brief
Modern
Delia Marchetti
Sales Representative
42 Calderwood Avenue, Ottawa, ON, K2P 3R6
delia_marchetti@quillmail.example
www.deliamarchetti.example
Space for personal photo (head shot) in the front
Office address and extra details on the back

```html
<!DOCTYPE html>
<html lang="en">
<head>
<meta charset="utf-8">
<title>Ambervale Homes – Business Card</title>
<link href="https://fonts.googleapis.com/css2?family=Libre+Baskerville:ital,wght@0,400;0,700;1,400&display=swap" rel="stylesheet">
<style>
  :root {
    --backdrop: #e6e9ec;
    --card: #ffffff;
    --ink: #1c1c1c;
    --gold: #a77a3a;
    --slate: #5c6b82;
    --map-tint: #dfe4ec;
    --photo-frame: #d7dbe0;
    --photo-fill: #8a7f7a;
  }
  * { margin: 0; padding: 0; box-sizing: border-box; }
  html, body {
    width: 1200px; height: 901px; overflow: hidden;
    background: var(--backdrop);
    font-family: "Libre Baskerville", Georgia, serif;
    color: var(--ink);
  }
  .stage {
    width: 1200px; height: 901px;
    display: flex; align-items: center; justify-content: center; gap: 60px;
  }
  .card {
    position: relative;
    width: 520px; height: 297px;
    background: var(--card);
    box-shadow: 0 12px 30px rgba(30, 40, 55, 0.16);
    overflow: hidden;
  }
  /* Back */
  .card-back { display: flex; align-items: center; justify-content: center; }
  .brand { display: flex; flex-direction: column; align-items: center; gap: 10px; }
  .brand-row { display: flex; align-items: center; gap: 12px; }
  .brand-dot { width: 22px; height: 22px; border-radius: 50%; background: var(--slate); }
  .brand-name {
    font-size: 34px; font-weight: 400; letter-spacing: 1px; color: var(--ink);
  }
  .brand-tagline {
    font-size: 8.5px; letter-spacing: 2px; text-transform: uppercase; color: var(--gold);
  }
  /* Front */
  .map-field {
    position: absolute; right: 0; top: 0; width: 62%; height: 100%;
    background: radial-gradient(ellipse at 60% 45%, var(--map-tint) 0%, rgba(223,228,236,0.5) 45%, rgba(255,255,255,0) 75%);
  }
  .front-left {
    position: absolute; left: 0; top: 0; width: 270px; height: 100%;
    display: flex; flex-direction: column; align-items: center; padding-top: 46px;
  }
  .front-left .brand-name { font-size: 20px; }
  .front-left .brand-dot { width: 13px; height: 13px; }
  .front-left .brand-tagline { font-size: 5.5px; letter-spacing: 1.3px; }
  .front-left .brand { gap: 6px; }
  .headshot {
    margin-top: 26px;
    width: 92px; height: 92px; border-radius: 14px;
    border: 5px solid var(--photo-frame);
    background: linear-gradient(160deg, #b3a69e, var(--photo-fill));
  }
  .divider {
    position: absolute; left: 278px; top: 40px; width: 1.5px; height: 217px;
    background: var(--gold);
  }
  .details {
    position: absolute; left: 296px; top: 52px; width: 210px;
    font-size: 9.5px; line-height: 1.55;
  }
  .person-name { font-size: 15px; color: var(--gold); line-height: 1.2; }
  .person-title { font-size: 9.5px; margin-bottom: 14px; }
  .address { margin-bottom: 12px; }
  .contact-label { display: inline-block; width: 14px; }
  .web { margin-top: 10px; }
</style>
</head>
<body>
<main class="stage">
  <section class="card card-back">
    <div class="brand">
      <div class="brand-row">
        <span class="brand-dot"></span>
        <span class="brand-name">Ambervale Homes inc</span>
      </div>
      <span class="brand-tagline">Brokerage Independently Owned and Operated</span>
    </div>
  </section>

  <section class="card card-front">
    <div class="map-field" role="img" aria-label="Faint world map background"></div>
    <div class="front-left">
      <div class="brand">
        <div class="brand-row">
          <span class="brand-dot"></span>
          <span class="brand-name">Ambervale Homes inc</span>
        </div>
        <span class="brand-tagline">Brokerage Independently Owned and Operated</span>
      </div>
      <div class="headshot" role="img" aria-label="Personal head shot photo of Delia Marchetti"></div>
    </div>
    <div class="divider"></div>
    <div class="details">
      <p class="person-name">Delia Marchetti</p>
      <p class="person-title">Sales Representative</p>
      <p class="address">42 Calderwood Avenue<br>Ottawa, ON, K2P 3R6</p>
      <p><span class="contact-label">P</span>613-555-0142</p>
      <p><span class="contact-label">C</span>613-555-0178</p>
      <p><span class="contact-label">F</span>613-555-0193</p>
      <p>delia_marchetti@quillmail.example</p>
      <p class="web">www.deliamarchetti.example</p>
    </div>
  </section>
</main>
</body>
</html>
```